Snooker/Billiards/CueSports Website - winner, second and 3rd paid!

We are looking to launch a website related to “cuesports”, especially snooker. Snooker is a popular sport in The UK and worldwide.

We are looking to build 2 pages with you for this contest

- the homepage
- and a page which will be used FOR EACH player we are working with and promoting (More below)

At the moment we have no idea about the design but it should be classy, ie. maybe similar to many of the high end fashion sites - maybe this kind of look?

https://www.vostrafind.co.uk/search?q=high+end+websites&espv=2&biw=1396&bih=694&source=lnms&tbm=isch&sa=X&ved=0ahUKEwiq6MaprYvPAhVoKcAKHW8mCiUQ_AUIBigB#tbm=isch&q=classy+websites

UNLESS THIS IS COMPLETELY THE WRONG IDEA FOR WHAT WE ARE DOING, we will leave it up to you to show us some of your best ideas and help us succeed!

We are more interested in the layout and design than the text at this stage. We can add gthe main text later with your help or by ourselves, but Design, look and feel is what we want to see for this contes. Obviously if you have any questions we will give you regular feedback during the time of this contest.

This will be an ecommerce site but we expect to get to the shopping cart stage in about a month

Our main marketing tool will be our website.

There are 3 core parts to our business in priority order:

1. Sales of Snooker/Billiards Equipment
We will be selling everything from the smallest items, snooker tips, chalk, to snooker cues (sticks) all the way to Major items such as snooker tables.

Here are some typical sites that sell snooker related equipment:

http://www.peterwelbeckbaizehall.com/
http://www.cuefervora.co.uk/
http://www.qrtbaize.co.uk/

2. Sale of our own branded fashion accessories: T’shirts, Caps, jackets, cologne etc etc

3. Our booking section, where we will promote famous snooker players and other sports stars for exhibitions, after dinner speaking, golf days, etc
(probably 1 page per player in the booking section with a picture, brief bio, summary of the kind of things they can be booked for and perhaps a tarrif sheet, though we may not publish this information online and prefer to ask people to contact us if they wish to book a player

Target Markets

Mainly the UK and Europe, but snooker is becoming increasingly popular in China

Demographics are mostly males aged 16 and 40

Logo Design (separate contest at a later time)

1. The design must project a sense of professionalism and have a high class feel

2. Must Have Priorities:

- Modern, professional and friendly.
- Strong emphasis on usability.
- mobile friendly - responsive

3. Should not Have:

- An anonymous cold and corporate feel.
- A too busy feel.

4. The winner of this design contest will also be awarded a freelance project to help us further develop/complete the site.

Thank You everyone and Good luck !

18-40 mainly

2 page

• - Modern, professional and friendly.
• - Strong emphasis on usability.
• - mobile friendly - responsive
• - An anonymous cold and corporate feel.
• - A too busy feel.

```html
<!DOCTYPE html>
<html lang="en">
<head>
<meta charset="utf-8">
<title>Cue Shop – Home</title>
<link href="https://fonts.googleapis.com/css2?family=Montserrat:wght@400;500;700;800&display=swap" rel="stylesheet">
<style>
:root{
  --red:#ef4646;
  --white:#ffffff;
  --ink:#111111;
  --dark:#232323;
  --footer:#1b1b1b;
  --grey-1:#2a2a2a;
  --grey-2:#5a5a5a;
  --grey-3:#9a9a9a;
  --grey-4:#d6d6d6;
}
*{margin:0;padding:0;box-sizing:border-box}
html,body{width:1200px;height:4775px;overflow:hidden}
body{font-family:"Montserrat",Arial,sans-serif;background:var(--white);color:var(--white);position:relative}
.abs{position:absolute}
.photo{position:absolute}

/* bands */
.band-red{position:absolute;left:0;top:0;width:1200px;height:1575px;background:var(--red)}
.band-dark{position:absolute;left:0;top:2992px;width:1200px;height:1330px;background:var(--dark)}
.band-subscribe{position:absolute;left:0;top:4322px;width:1200px;height:128px;background:var(--red)}
.band-footer{position:absolute;left:0;top:4450px;width:1200px;height:325px;background:var(--footer)}

/* header */
.menu-toggle{left:25px;top:19px;width:45px;height:38px}
.header-action{width:70px;text-align:center;top:22px;font-size:13px;color:var(--ink)}
.header-action svg{display:block;margin:0 auto 6px;width:44px;height:44px}

/* hero collage */
.hero-headline{font-weight:800;font-size:60px;line-height:74px;color:var(--white);letter-spacing:1px}
.brand-tile{left:481px;top:239px;width:238px;height:232px;background:var(--red);display:flex;align-items:center;justify-content:center;font-weight:700;font-size:48px}

.intro{left:223px;top:762px;width:764px;text-align:center;font-weight:700;font-size:24px;line-height:36px}

/* winner band */
.winner-title{left:121px;top:1066px;font-weight:800;font-size:56px;line-height:75px}
.winner-text{left:200px;top:1322px;width:900px;text-align:center;font-weight:700;font-size:24px;line-height:36px}

/* rule the board */
.rule-copy{left:430px;top:1607px;width:340px;height:640px;background:var(--white);color:var(--ink);display:flex;align-items:center;justify-content:center;padding:0 28px;text-align:center;font-weight:700;font-size:26px;line-height:36px}
.rule-title{left:102px;top:1865px;font-weight:800;font-size:56px;line-height:70px}

.section-title{left:0;width:1200px;text-align:center;font-weight:800;font-size:56px;color:var(--red)}

/* categories */
.category{position:absolute;top:2610px;width:240px;height:382px}
.category-name{position:absolute;left:0;right:0;top:208px;text-align:center;font-weight:800;font-size:25px;line-height:28px;color:var(--white);letter-spacing:.5px}
.shop-now{position:absolute;left:62px;top:295px;width:115px;height:30px;border:2px solid var(--white);font-size:13px;display:flex;align-items:center;justify-content:center;color:var(--white)}

/* community */
.story-overlay{position:absolute;font-weight:800;font-size:34px;line-height:38px;text-align:center;color:var(--white)}
.story-rule{position:absolute;width:8px;background:var(--white)}
.story-text{position:absolute;font-size:16px;line-height:21px;color:var(--white)}
.read-more{left:525px;top:4217px;width:178px;height:48px;border:2px solid var(--white);display:flex;align-items:center;justify-content:center;font-size:20px}

/* subscribe */
.subscribe-title{left:0;top:4350px;width:1200px;text-align:center;font-weight:800;font-size:29px}
.subscribe-input{left:372px;top:4404px;width:332px;height:24px;background:var(--white);border-radius:12px}
.subscribe-button{left:726px;top:4404px;width:140px;height:24px;background:var(--ink);border-radius:12px;font-size:13px;display:flex;align-items:center;justify-content:center}

/* footer */
.footer-links{font-size:19px;line-height:42px;list-style:none}
.footer-rule{position:absolute;width:8px;background:var(--white)}
.footer-logo{left:525px;top:4550px;width:191px;height:80px;border:2px solid var(--white);display:flex;align-items:center;justify-content:center;font-weight:700;font-size:38px}
.footer-small{font-size:19px;line-height:25px}
.copyright{left:0;top:4728px;width:1200px;text-align:center;font-size:18px}
</style>
</head>
<body>

<div class="band-red"></div>

<!-- header -->
<svg class="abs menu-toggle" viewBox="0 0 45 38" aria-label="Menu">
  <rect x="0" y="2" width="45" height="7" fill="#111"/>
  <rect x="0" y="15" width="45" height="7" fill="#111"/>
  <rect x="0" y="28" width="45" height="7" fill="#111"/>
</svg>
<div class="abs header-action" style="left:1013px">
  <svg viewBox="0 0 44 44" aria-hidden="true">
    <path d="M4 8h7l5 20h20l4-14H13" fill="none" stroke="#111" stroke-width="3.5" stroke-linejoin="round"/>
    <circle cx="18" cy="36" r="3.5" fill="#111"/><circle cx="33" cy="36" r="3.5" fill="#111"/>
  </svg>Cart</div>
<div class="abs header-action" style="left:1108px">
  <svg viewBox="0 0 44 44" aria-hidden="true">
    <circle cx="22" cy="22" r="18" fill="none" stroke="#111" stroke-width="3.5" stroke-dasharray="6 3"/>
    <line x1="14" y1="30" x2="30" y2="14" stroke="#111" stroke-width="3.5"/>
    <circle cx="15" cy="16" r="3.5" fill="#111"/><circle cx="29" cy="28" r="3.5" fill="#111"/>
  </svg>Discount</div>

<!-- hero collage -->
<div class="photo" role="img" aria-label="Black eight ball on a dark table" style="left:245px;top:0;width:236px;height:471px;background:radial-gradient(circle at 45% 20%,#6a6a6a,#1b1b1b 60%,#0d0d0d)"></div>
<div class="photo" role="img" aria-label="Eight ball on cloth, close-up" style="left:481px;top:0;width:474px;height:239px;background:linear-gradient(160deg,#f2f2f2,#bdbdbd 45%,#555 100%)"></div>
<div class="photo" role="img" aria-label="Row of cues in a rack" style="left:719px;top:239px;width:236px;height:232px;background:linear-gradient(135deg,#3a3a3a,#8a8a8a 55%,#2a2a2a)"></div>
<div class="photo" role="img" aria-label="Cue butts lined up on a dark background" style="left:481px;top:471px;width:474px;height:236px;background:linear-gradient(120deg,#1a1a1a,#555 50%,#1c1c1c)"></div>
<div class="abs brand-tile">logo</div>
<div class="abs hero-headline" style="left:255px;top:252px">PLAY<br>YOUR<br>WAY</div>
<div class="abs hero-headline" style="left:512px;top:482px">BUY<br>YOUR<br>WAY</div>

<p class="abs intro">Lorem ipsum dolor sit amet, consectetur adipiscing elit. Vivamus ut nunc lorem. Cras ac tincidunt nibh. Mauris aliquam diam ac justo volutpat, et consectetur est commodo. Curabitur a dui diam. Curabitur facilisis sapien ac tempor congue. Vi-</p>

<!-- be the winner -->
<div class="photo" role="img" aria-label="Crossed cues beside a cluster of pool balls" style="left:51px;top:1003px;width:1149px;height:541px;background:linear-gradient(100deg,#1c1c1c,#3b3b3b 45%,#6e6e6e 75%,#2b2b2b)"></div>
<h2 class="abs winner-title">BE<br>THE<br>WINNER</h2>
<p class="abs winner-text">Lorem ipsum dolor sit amet, consectetur adipiscing elit. Vivamus ut nunc lorem. Cras ac tincidunt nibh. Mauris aliquam diam ac justo volutpat, et consectetur est commodo. Curabitur a dui diam. Curabitur facilisis sapien ac tempor congue. Vi-</p>

<!-- rule the board -->
<div class="photo" role="img" aria-label="Player's hand lining up a cue on the table" style="left:0;top:1607px;width:430px;height:640px;background:linear-gradient(150deg,#5c5c5c,#2a2a2a 50%,#141414)"></div>
<div class="photo" role="img" aria-label="White cue ball on the cloth" style="left:770px;top:1607px;width:430px;height:640px;background:radial-gradient(circle at 70% 75%,#d9d9d9,#6a6a6a 30%,#1e1e1e 75%)"></div>
<p class="abs rule-copy">Lorem ipsum dolor sit amet, consectetur adipiscing elit. Vivamus ut nunc lorem. Cras ac tincidunt nibh. Mauris aliquam diam ac justo volutpat, et consectetur est commodo. Curabitur a dui diam. Curabitur facilisis</p>
<h2 class="abs rule-title">RULE<br>THE<br>BOARD</h2>

<h2 class="abs section-title" style="top:2455px">GET THE WINNING RIG</h2>

<!-- categories -->
<div class="category" style="left:0" role="img" aria-label="Accessories on a green table">
  <div class="photo" style="inset:0;background:linear-gradient(160deg,#5b1d1d,#1f3b22 55%,#0e1a10)"></div>
  <div class="category-name">ACCESSORIES</div><div class="shop-now">SHOP NOW</div>
</div>
<div class="category" style="left:240px" role="img" aria-label="Cues on green cloth">
  <div class="photo" style="inset:0;background:linear-gradient(120deg,#0f4a14,#2f8a2a 50%,#0c3a10)"></div>
  <div class="category-name">CUES</div><div class="shop-now">SHOP NOW</div>
</div>
<div class="category" style="left:480px" role="img" aria-label="Racked coloured balls">
  <div class="photo" style="inset:0;background:linear-gradient(140deg,#7a1717,#2b2b5a 45%,#8a6a12 75%,#1b1b1b)"></div>
  <div class="category-name">BALLS</div><div class="shop-now">SHOP NOW</div>
</div>
<div class="category" style="left:720px" role="img" aria-label="Tables in assorted cloth colours">
  <div class="photo" style="inset:0;background:linear-gradient(135deg,#3b5f8a,#6a3f8a 45%,#2c6a6a 75%,#1e1e1e)"></div>
  <div class="category-name">TABLES</div><div class="shop-now">SHOP NOW</div>
</div>
<div class="category" style="left:960px" role="img" aria-label="Cue cases lined up">
  <div class="photo" style="inset:0;background:linear-gradient(150deg,#6a6a6a,#2a2a2a 45%,#6b1414 80%)"></div>
  <div class="category-name">POOL &amp;<br>CUE CASES</div><div class="shop-now">SHOP NOW</div>
</div>

<!-- community -->
<div class="band-dark"></div>
<h2 class="abs section-title" style="top:3095px">Communinty</h2>

<div class="photo" role="img" aria-label="Champion holding a trophy" style="left:48px;top:3196px;width:821px;height:404px;background:linear-gradient(110deg,#5a0f1f,#2c1522 45%,#4a2a2a 70%,#1a1a1a)"></div>
<div class="story-overlay" style="left:720px;top:3380px;width:150px">Lorem ipsum dolor sit amet, con-</div>
<div class="story-rule" style="left:875px;top:3215px;height:375px"></div>
<p class="story-text" style="left:891px;top:3205px;width:292px">Lorem ipsum dolor sit amet, consectetur adipiscing elit. Nunc ut ligula non lorem egestas bibendum eget id est. Sed erat odio, suscipit sit amet augue sed, luctus efficitur odio. Nunc commodo turpis in felis posuere, a imperdiet urna sagittis. Curabitur tempus mi egestas mi tincidunt elementum. Donec vitae quam mauris. Curabitur eget nunc ut felis pulvinar fringilla vitae tempus purus. Praesent sollicitudin, mauris</p>

<div class="photo" role="img" aria-label="Player posing with a trophy" style="left:54px;top:3623px;width:277px;height:522px;background:linear-gradient(170deg,#3a2a22,#2a4a2a 55%,#0f3a14)"></div>
<div class="story-overlay" style="left:110px;top:3710px;width:210px">Lorem ipsum dolor sit amet, con-</div>
<div class="story-rule" style="left:341px;top:3623px;height:290px"></div>
<p class="story-text" style="left:356px;top:3628px;width:315px">Lorem ipsum dolor sit amet, consectetur adipiscing elit. Nunc ut ligula non lorem egestas bibendum eget id est. Sed erat odio, suscipit sit amet augue sed, luctus efficitur odio. Nunc commodo turpis in felis posuere, a imperdiet urna sagittis. Curabitur tempus mi egestas mi tincidunt elementum. Donec vitae quam mauris. Curabitur eget nunc.</p>

<div class="photo" role="img" aria-label="Player leaning over the table to take a shot" style="left:691px;top:3623px;width:493px;height:267px;background:linear-gradient(160deg,#2a2a2a,#1f5a24 55%,#0e3a12)"></div>

<div class="photo" role="img" aria-label="Player smiling at the table" style="left:356px;top:3901px;width:318px;height:243px;background:linear-gradient(150deg,#3a2a1a,#2a1a14 50%,#5a1414)"></div>
<div class="story-overlay" style="left:520px;top:3965px;width:150px">Lorem ipsum dolor sit amet, con-</div>
<div class="story-rule" style="left:687px;top:3910px;height:230px"></div>
<p class="story-text" style="left:703px;top:3950px;width:480px">Lorem ipsum dolor sit amet, consectetur adipiscing elit. Nunc ut ligula non lorem egestas bibendum eget id est. Sed erat odio, suscipit sit amet augue sed, luctus efficitur odio. Nunc commodo turpis in felis posuere, a imperdiet urna sagittis. Curabitur tempus mi egestas mi tincidunt elementum. Donec vitae quam mauris. Curabitur eget nunc ut felis pulvinar fringilla vitae tempus purus. Praesent sollicitudin, mauris id sodales fermentum, purus quam varius orci, id commodo metus sem sit amet ipsum. Etiam ut feli</p>

<div class="abs read-more">Read more</div>

<!-- subscribe -->
<div class="band-subscribe"></div>
<div class="abs subscribe-title">SUBSCRIBE NOW FOR NEWS &amp; LATEST OFFERS</div>
<div class="abs subscribe-input"></div>
<div class="abs subscribe-button">Subscribe now</div>

<!-- footer -->
<div class="band-footer"></div>
<ul class="abs footer-links" style="left:99px;top:4494px">
  <li>Home</li><li>Site Map</li><li>Shop Now</li><li>Community</li><li>Contact us</li>
</ul>
<div class="footer-rule" style="left:240px;top:4500px;height:150px"></div>
<ul class="abs footer-links" style="left:286px;top:4494px">
  <li>Support</li><li>Feedback us</li><li>Facepage page</li><li>Chirper account</li>
</ul>
<div class="abs footer-logo">Logo</div>
<div class="abs footer-small" style="left:853px;top:4537px">Follow us<br>Facepage,<br>Chirper</div>
<div class="footer-rule" style="left:964px;top:4520px;height:130px"></div>
<div class="abs footer-small" style="left:1003px;top:4525px">Address:<br>Door no. 123,<br>Street  name,<br>City - 123456,<br>Country.</div>
<div class="abs copyright">Copyright © 2016 Cue shop</div>

</body>
</html>
```